LumaPeak business card

We are a performing arts company providing training (to both kids and adults) as well as performers for events. We hope to bring joy and confidence on stage to the people we train, as well as joy to the audience when our artistes perform. Designs should convey the joy, confidence and vibrancy on stage. Design business card using the attached logo. Card to include name, mobile tel, email address, company address, and website. Double sided. To also include the following list of what the company does:
• Training & Enrichment
• Private & Corporate Entertainment
- Music composition & production

Industry/Entity Type

Training

Contact Information for Business Card

Card to include name, mobile tel, email address, company address, and website. Double sided. To also include the following list of what the company does:
• Training & Enrichment

Requirements
Nice to have
• Card need not be the traditional rectangular in shape but not too outrageous.

```html
<!DOCTYPE html>
<html lang="en">
<head>
<meta charset="utf-8">
<title>LumaPeak business card</title>
<link href="https://fonts.googleapis.com/css2?family=Questrial&display=swap" rel="stylesheet">
<style>
  :root {
    --bg: #6f6f72;
    --bg-light: #838386;
    --card: #0b0b0b;
    --ink-grey: #3a3a3a;
    --cyan: #1aa7e0;
    --yellow: #f5b400;
    --red: #e8283c;
    --green: #3fb44a;
    --blue: #2a5bb8;
    --purple: #a23aa6;
    --tagline: #3b6fc4;
    --brand: #f2a20f;
  }
  * { margin: 0; padding: 0; box-sizing: border-box; }
  html, body { width: 1200px; height: 900px; overflow: hidden; }
  body {
    background: radial-gradient(ellipse at 50% 40%, var(--bg-light), var(--bg));
    font-family: "Questrial", "Century Gothic", sans-serif;
    position: relative;
  }
  .card {
    position: absolute;
    top: 300px;
    width: 520px;
    height: 300px;
    background: var(--card);
    border-radius: 4px;
    box-shadow: 0 14px 30px rgba(0,0,0,.35);
    overflow: hidden;
  }
  .card--front { left: 60px; }
  .card--back { left: 620px; }

  /* front */
  .brand {
    position: absolute;
    top: 62px;
    left: 0;
    width: 100%;
    display: flex;
    align-items: center;
    justify-content: center;
    gap: 14px;
  }
  .brand__mark {
    width: 34px; height: 34px;
    border-radius: 50%;
    background: var(--brand);
  }
  .brand__name {
    font-size: 54px;
    color: var(--brand);
    letter-spacing: 1px;
    line-height: 1;
  }
  .tagline {
    position: absolute;
    top: 130px;
    width: 100%;
    text-align: center;
    color: var(--tagline);
    font-size: 17px;
    font-style: italic;
  }
  .front-motif {
    position: absolute;
    left: 50%;
    bottom: 26px;
    width: 96px; height: 96px;
    margin-left: -48px;
    border-radius: 50%;
    background: var(--ink-grey);
  }

  /* back */
  .back-art {
    position: absolute;
    top: 0; left: 0;
    width: 100%;
    height: 150px;
    background: linear-gradient(110deg, #f3b300 0%, #1d4fa8 40%, #1a8fd6 65%, #e8283c 100%);
    opacity: .9;
  }
  .contact {
    position: absolute;
    left: 26px;
    top: 168px;
    list-style: none;
    font-size: 16px;
    line-height: 1.25;
  }
  .contact__tel { color: var(--cyan); }
  .contact__web { color: var(--yellow); }
  .contact__mail { color: var(--red); }
  .services {
    position: absolute;
    left: 26px;
    top: 234px;
    list-style: none;
    font-size: 12.5px;
    line-height: 1.3;
  }
  .services li::before { content: "• "; }
  .services__training { color: var(--green); }
  .services__events { color: var(--blue); }
  .services__music { color: var(--purple); }
</style>
</head>
<body>
  <section class="card card--front">
    <div class="brand">
      <span class="brand__mark"></span>
      <span class="brand__name">LumaPeak</span>
    </div>
    <p class="tagline">delighting in the arts</p>
    <div class="front-motif"></div>
  </section>

  <section class="card card--back">
    <div class="back-art" role="img" aria-label="Colourful illustration of dancing performers and musical notes"></div>
    <ul class="contact">
      <li class="contact__tel">T: +34 611 482 730</li>
      <li class="contact__web">W: lumapeak-arts.com</li>
      <li class="contact__mail">M: hola@lumapeak-arts.com</li>
    </ul>
    <ul class="services">
      <li class="services__training">Training &amp; Enrichment</li>
      <li class="services__events">Private &amp; Corporate Entertainment</li>
      <li class="services__music">Music composition &amp; production</li>
    </ul>
  </section>
</body>
</html>
```